Webdesign für Personalberatung
Zielgruppe
Personalberatung Headhunting. Zielgruppe: Personalleiter / Geschäftsführer , die Kandidaten suchen und nicht finden
Aufgabenstellung
Die Webseite soll vermitteln:
- Vertrauen/Verlässlichkeit
- Kompetenz
- Internationalität
- Langjährige Erfahrung
- Aktuelle Trends umsetzend
- Seriosität
- Pragmatismus/Problemlöser
- Nachhaltigkeit
Was wir nicht wollen ist eine 0815 Personalberater / Zeitarbeit Seite

```html
<!DOCTYPE html>
<html lang="de">
<head>
<meta charset="utf-8">
<title>Stellenanzeigen – Meridian Recruiters</title>
<link rel="stylesheet" href="https://fonts.googleapis.com/css2?family=Arimo:wght@400&family=Noto+Sans:wght@400;700&display=swap">
<style>
  :root {
    --ink: #444444;
    --nav-ink: #3f3f3f;
    --accent: #c99a63;
    --sand: #f5efe6;
    --field-border: #9a9a9a;
    --white: #ffffff;
  }
  * { margin: 0; padding: 0; box-sizing: border-box; }
  html, body { width: 1200px; height: 675px; overflow: hidden; background: var(--white); }
  .page { position: relative; width: 1200px; height: 675px; font-family: "Noto Sans", sans-serif; color: var(--ink); }

  .nav-indicator { position: absolute; left: 215px; top: 0; width: 97px; height: 3px; background: var(--accent); }
  .nav-item { position: absolute; top: 81px; transform: translateX(-50%); font-family: "Arimo", sans-serif; font-size: 16px; color: var(--nav-ink); white-space: nowrap; letter-spacing: -0.2px; }
  .nav-item.is-active { color: var(--accent); }

  .brand { position: absolute; left: 600px; top: 77px; transform: translateX(-50%); font-family: "Arimo", sans-serif; font-weight: 400; font-size: 21px; line-height: 26px; color: var(--nav-ink); white-space: nowrap; }

  .hero { position: absolute; left: 0; top: 142px; width: 1200px; height: 114px; background: var(--sand); text-align: center; }
  .hero-title { margin-top: 10px; font-size: 50px; font-weight: 700; line-height: 60px; color: var(--ink); }
  .hero-lead { margin-top: 2px; font-size: 15px; color: var(--ink); }

  .search-panel { position: absolute; left: 305px; top: 307px; width: 591px; height: 164px; background: var(--sand); }
  .search-label { position: absolute; top: 11px; font-size: 28px; font-weight: 400; color: var(--ink); }
  .search-label.fulltext { left: 22px; }
  .search-label.region { left: 315px; }
  .search-input, .region-select { position: absolute; top: 53px; width: 207px; height: 27px; border: 1px solid var(--field-border); background: var(--white); font-family: "Noto Sans", sans-serif; font-size: 13px; }
  .search-input { left: 29px; padding: 0 2px; color: #8a8a8a; display: flex; align-items: center; }
  .region-select { left: 317px; padding: 0 6px; color: #222; display: flex; align-items: center; justify-content: space-between; font-size: 14px; }
  .region-select .caret { font-size: 10px; }
  .search-button { position: absolute; left: 29px; top: 113px; width: 51px; height: 28px; border: 1px solid var(--field-border); background: var(--white); font-family: "Noto Sans", sans-serif; font-size: 13px; color: #222; display: flex; align-items: center; justify-content: center; }
</style>
</head>
<body>
<div class="page">
  <header class="site-header">
    <div class="nav-indicator"></div>
    <nav>
      <span class="nav-item" style="left:109px">Über uns</span>
      <span class="nav-item is-active" style="left:263px">Stellenbörse</span>
      <span class="nav-item" style="left:421px">Mitglieder</span>
      <span class="nav-item" style="left:776px">Aktuelles</span>
      <span class="nav-item" style="left:912px">Dienstleistungen</span>
      <span class="nav-item" style="left:1088px">Qualitätsgrundsätze</span>
    </nav>
    <div class="brand">Meridian Recruiters</div>
  </header>

  <section class="hero">
    <h1 class="hero-title">Stellenanzeigen</h1>
    <p class="hero-lead">Wir bieten Ihnen die perfekte Stelle in Ihrer Umgebung, fair, sicher und einfach!</p>
  </section>

  <section class="search-panel">
    <h2 class="search-label fulltext">Volltextsuche</h2>
    <h2 class="search-label region">Region</h2>
    <div class="search-input">Suchbegriff</div>
    <div class="region-select"><span>Bitte auswählen</span><span class="caret">▼</span></div>
    <div class="search-button">Suchen</div>
  </section>
</div>
</body>
</html>
```